Pelverhook LLC
Business Cards & Stationary
Professional
Tobias Wendell
President
482 Orchard Crest Road
Dunmore Falls, NJ 07934-2718
tobias.wendell@mailvexo.com
www.pelverhook.com
I require the full suite of stationary products i.e.:- Business card, letterhead, envelope, fax cover sheet, thank you cards, invoice etc.
Just the logo on the back of the card.

```html
<!DOCTYPE html>
<html lang="en">
<head>
<meta charset="utf-8">
<title>Pelverhook LLC — Business Card</title>
<link href="https://fonts.googleapis.com/css2?family=Roboto+Condensed:wght@400;700&display=swap" rel="stylesheet">
<style>
  :root {
    --backdrop: #e8e4dd;
    --card: #ffffff;
    --blue-deep: #174f9c;
    --blue-mid: #2f6fc0;
    --blue-light: #8fb4e0;
    --ink-blue: #1b5aa8;
    --ink-dark: #2b2b2b;
    --rule: #c9ced6;
  }
  * { box-sizing: border-box; margin: 0; padding: 0; }
  html, body { width: 1200px; height: 780px; overflow: hidden; background: var(--backdrop); }
  body { font-family: "Roboto Condensed", "Arial Narrow", sans-serif; position: relative; }

  .business-card {
    position: absolute; left: 60px; top: 82px;
    width: 1080px; height: 617px;
    background: var(--card);
    border-radius: 30px;
    box-shadow: 0 4px 18px rgba(0,0,0,0.12);
    overflow: hidden;
  }
  .brand-band { position: absolute; left: 0; top: 0; width: 1080px; height: 300px; }

  .brand-name {
    position: absolute; left: 0; width: 1080px; top: 262px;
    text-align: center; color: var(--ink-blue);
    font-weight: 400; font-size: 70px; letter-spacing: 2px; text-transform: uppercase;
    line-height: 1;
  }
  .brand-name .suffix { font-size: 22px; letter-spacing: 1px; }

  .divider {
    position: absolute; left: 548px; top: 392px; width: 2px; height: 170px;
    background: var(--rule);
  }

  .holder {
    position: absolute; right: 562px; top: 392px; text-align: right;
    color: var(--ink-dark); font-size: 25px; line-height: 1.3;
  }
  .holder .person { color: var(--ink-blue); font-weight: 700; font-size: 31px; }
  .holder .role { color: var(--ink-blue); font-weight: 700; font-size: 26px; margin-bottom: 10px; }

  .contacts { position: absolute; left: 572px; top: 394px; list-style: none; }
  .contacts li {
    display: flex; align-items: center; gap: 12px;
    height: 37px; font-size: 25px; color: var(--ink-dark);
  }
  .contacts svg { width: 22px; height: 22px; flex: none; fill: var(--ink-blue); }
</style>
</head>
<body>
  <div class="business-card">
    <svg class="brand-band" viewBox="0 0 1080 300" aria-hidden="true">
      <defs>
        <linearGradient id="bandFill" x1="0" y1="0" x2="0" y2="1">
          <stop offset="0" stop-color="#3a7bcc"/>
          <stop offset="0.5" stop-color="#174f9c"/>
          <stop offset="1" stop-color="#2c68b6"/>
        </linearGradient>
        <radialGradient id="markFill" cx="0.5" cy="0.4" r="0.6">
          <stop offset="0" stop-color="#4f88cf"/>
          <stop offset="1" stop-color="#1c4f93"/>
        </radialGradient>
      </defs>
      <rect x="0" y="58" width="1080" height="8" fill="var(--blue-light)"/>
      <rect x="0" y="70" width="1080" height="118" fill="url(#bandFill)"/>
      <rect x="0" y="192" width="1080" height="8" fill="var(--blue-light)"/>
      <circle cx="530" cy="150" r="98" fill="url(#markFill)"/>
    </svg>

    <div class="brand-name">Pelverhook <span class="suffix">LLC</span></div>

    <div class="holder">
      <div class="person">Tobias Wendell</div>
      <div class="role">President</div>
      <div>482 Orchard Crest Road</div>
      <div>Dunmore Falls, NJ 07934-2718</div>
    </div>

    <div class="divider"></div>

    <ul class="contacts">
      <li>
        <svg viewBox="0 0 24 24" aria-label="Phone"><path d="M6.6 10.8a15.1 15.1 0 0 0 6.6 6.6l2.2-2.2a1 1 0 0 1 1-.25 11.4 11.4 0 0 0 3.6.57 1 1 0 0 1 1 1V20a1 1 0 0 1-1 1A17 17 0 0 1 3 4a1 1 0 0 1 1-1h3.5a1 1 0 0 1 1 1c0 1.25.2 2.45.57 3.6a1 1 0 0 1-.25 1z"/></svg>
        <span>555.318.4620</span>
      </li>
      <li>
        <svg viewBox="0 0 24 24" aria-label="Mobile"><path d="M7 1h10a2 2 0 0 1 2 2v18a2 2 0 0 1-2 2H7a2 2 0 0 1-2-2V3a2 2 0 0 1 2-2zm0 3v14h10V4zm5 15.5a1.2 1.2 0 1 0 0 2.4 1.2 1.2 0 0 0 0-2.4z"/></svg>
        <span>555.762.9031</span>
      </li>
      <li>
        <svg viewBox="0 0 24 24" aria-label="Fax"><path d="M7 2h9l3 3v5H7zm-3 9h16a2 2 0 0 1 2 2v7a2 2 0 0 1-2 2H4a2 2 0 0 1-2-2v-7a2 2 0 0 1 2-2zm2 3v2h3v-2zm0 4v2h3v-2zm5-4v2h7v-2z"/></svg>
        <span>555.318.4620</span>
      </li>
      <li>
        <svg viewBox="0 0 24 24" aria-label="Email"><path d="M2 5h20v14H2zm2 2v.5l8 5 8-5V7zm0 2.8V17h16V9.8l-8 5z"/></svg>
        <span>tobias.wendell@mailvexo.com</span>
      </li>
    </ul>
  </div>
</body>
</html>
```